Nora Pettifer Music EP Design Artwork

EP musical recording cover art work. Nora Pettifer is a new artist in the Pop, Country Pop, Pop Rock, Americana and Singer-songwriter genres. The name of the EP is "Where the River Bends", and her first single is being released on all streaming platforms globally June 1st. We are looking for a graphic design that has that Pop/rock female artist appeal. norapettifer.net and all social media outlets are norapettifersongs (reference). Your art work will be seen globally and we will give a personal shout out on all her socials to the design we select as a single post. Her signature logo is attached for a color and style example. Please try to use the signature within the EP cover design, but feel free to change the purple backing accordingly if another color is needed to fit better with the color scheme of your design.

Requirements
Must have
• Nora Pettifer signature logo and EP name

Some of you asked for hi res pics, use this link:

https://files.quillbox.net/share/u/0/folders/8kTzW3pLqR2vN7xYcD4mHs1JbE6uAfGoQ
Should not have
• June 1 on the EP art work. June 1 is the release of the first single on the EP. This is an album cover, we want it to look like a really cool pop female artist album cover, thanks.

```html
<!DOCTYPE html>
<html lang="en">
<head>
<meta charset="utf-8">
<title>Where the River Bends — Nora Pettifer</title>
<link rel="stylesheet" href="https://fonts.googleapis.com/css2?family=Bungee&display=swap">
<style>
  :root {
    --paper: #ffffff;
    --ink: #1e1b3d;
    --pop-red: #e8344a;
    --pop-blue: #1f5fb5;
    --pop-orange: #f07d22;
    --pop-yellow: #f5a623;
    --pop-teal: #5cc6c7;
    --title-face: #47c4c6;
    --title-side: #f7d23a;
    --title-edge: #e63950;
    --portrait-light: #d9b98a;
    --portrait-dark: #1a1f2e;
    --frame: #ffffff;
  }
  html, body {
    margin: 0;
    padding: 0;
    overflow: hidden;
    background: var(--paper);
  }
  .cover {
    position: relative;
    width: 1200px;
    height: 1200px;
    overflow: hidden;
    background: var(--paper);
  }
  .cover__panels,
  .cover__portrait {
    position: absolute;
    inset: 0;
    width: 1200px;
    height: 1200px;
  }
  .panel { stroke: var(--ink); stroke-width: 3; stroke-linejoin: round; }
  .panel--red { fill: var(--pop-red); }
  .panel--blue { fill: var(--pop-blue); }
  .panel--orange { fill: var(--pop-orange); }
  .panel--yellow { fill: var(--pop-yellow); }
  .panel--teal { fill: var(--pop-teal); }

  .ep-title {
    position: absolute;
    left: 88px;
    top: 100px;
    margin: 0;
    font-family: "Bungee", sans-serif;
    font-weight: 400;
    font-size: 94px;
    line-height: 104px;
    letter-spacing: 2px;
    text-transform: uppercase;
    color: var(--title-face);
    -webkit-text-stroke: 2px var(--ink);
    text-shadow:
      3px 3px 0 var(--title-side),
      5px 5px 0 var(--title-side),
      7px 7px 0 var(--title-edge),
      9px 9px 0 var(--title-edge),
      10px 10px 0 var(--ink);
  }
  .ep-title__line { display: block; }

  .artist-name {
    position: absolute;
    left: 590px;
    top: 1010px;
    margin: 0;
    font-family: "Bungee", sans-serif;
    font-weight: 400;
    font-size: 54px;
    color: var(--frame);
  }
</style>
</head>
<body>
<main class="cover">
  <svg class="cover__panels" viewBox="0 0 712 712" aria-hidden="true">
    <polygon class="panel panel--red" points="150,0 345,0 300,195"/>
    <polygon class="panel panel--blue" points="345,0 600,0 350,62"/>
    <polygon class="panel panel--teal" points="345,62 382,150 330,110"/>
    <polygon class="panel panel--orange" points="350,62 712,0 712,40 610,110 382,150"/>
    <polygon class="panel panel--red" points="610,110 712,40 712,175 650,180"/>
    <polygon class="panel panel--yellow" points="545,110 610,110 650,180 712,175 712,590 600,600"/>
    <polygon class="panel panel--orange" points="600,600 712,590 712,712 650,712"/>
    <polygon class="panel panel--teal" points="0,525 225,430 240,500 0,575"/>
    <polygon class="panel panel--blue" points="0,575 240,500 205,712 0,712"/>
  </svg>

  <svg class="cover__portrait" viewBox="0 0 712 712" role="img" aria-label="Portrait photograph of the artist in a dark denim jacket and patterned scarf, cut out with a white border">
    <defs>
      <linearGradient id="portraitTone" x1="0" y1="0" x2="0" y2="1">
        <stop offset="0" stop-color="var(--portrait-light)"/>
        <stop offset="0.45" stop-color="#c89f74"/>
        <stop offset="0.6" stop-color="var(--portrait-dark)"/>
        <stop offset="1" stop-color="var(--portrait-dark)"/>
      </linearGradient>
    </defs>
    <path d="M330,170 C322,110 360,92 418,92 C480,92 520,120 522,190 C526,260 540,320 560,360 C610,390 640,440 655,520 C668,600 672,660 676,712 L170,712 C166,640 160,560 180,470 C198,400 250,370 300,350 C318,300 334,240 330,170 Z"
          fill="url(#portraitTone)" stroke="var(--frame)" stroke-width="8" stroke-linejoin="round"/>
  </svg>

  <h1 class="ep-title">
    <span class="ep-title__line">Where</span>
    <span class="ep-title__line">The</span>
    <span class="ep-title__line">River</span>
    <span class="ep-title__line">Bends</span>
  </h1>

  <p class="artist-name">Nora Pettifer</p>
</main>
</body>
</html>
```